Thoroughbred Racing Partnership needs web design

Crest of Fortune Partners is a management group who buys horses and races them on both the West and East coasts. The premise of the business is for an investment as little as $500, anyone can be a partner and own a percentage of a horse(s). This is a low cost way of getting involved in the exciting sport of Thoroughbred Racing, without shouldering the heavy financial responsibility. Our target market is mostly males 40+ but we want to include all target markets. We are looking for something very clean and professional, we want to give an image of success. Nothing overly "artsy." I have included the logo in which you can incorporate in the site. Also, the logo colors will be the colors of our "silks." The silks are what the jockey wears and will be an important marketing tool for COF. We would like a very prominent picture of a racehorse somewhere on the homepage, we want to make it clear that is a website for Horseracing partnerships.

On the top of the site, it should say "Crest of Fortune" (on the top)
and below that "Thoroughbred Racing Partnerships." (below that)

The main sections, which should be across the top are:

Home
About Us
Ownership
Stable Roster
News
Contact us

Some of these will have drop down menus.

An example of a competitor website that we like is: www.harlowfieldeq.example
An example of a competitor website that we don't like is: www.gallopvane.example
Updates

Project Deadline Extended
Reason: We have a Board of Directors meeting on the 22nd and we will be making a decision on that day. I'm giving an extension so that all designers are able to submit their designs by the 22nd. Thank you!

Target Market(s)

40+ males

Industry/Entity Type

Business

Requirements
Must have
• our logo must be on the site. We would like at least one bold image of a thoroughbred horse in action. The picture is going to tell the story so it needs to be very eye-catching.

Our slogan should also be included on the website, "Experience the thrill of owning a Racehorse."
Should not have
• cartoons, artsy pictures, pictures of Steeplechase horses or "jumpers." This partnership is for racehorses only, there is not jumping involved with the horses.

```html
<!DOCTYPE html>
<html lang="en">
<head>
<meta charset="utf-8">
<title>Crest of Fortune Partners — Thoroughbred Racing Partnerships</title>
<link rel="stylesheet" href="https://fonts.googleapis.com/css2?family=Arvo:wght@400;700&family=Source+Sans+3:wght@300;400;600&family=Open+Sans:ital,wght@0,400;0,600;1,700&display=swap">
<style>
:root{
  --gold:#e0a419;
  --gold-dark:#c98f0e;
  --ink:#ffffff;
  --muted:#bdbdbd;
  --topbar:#1a1a1a;
  --header:#151515;
  --page:#262626;
  --panel-dark:#111111;
  --panel-grey:#343434;
  --footer:#232323;
  --bottom:#1b1b1b;
  --line:#444;
}
*{box-sizing:border-box;margin:0;padding:0}
html,body{width:1200px;height:2347px;overflow:hidden}
body{position:relative;background:var(--page);color:var(--ink);font-family:"Open Sans",sans-serif}
.abs{position:absolute}

.topbar{left:0;top:0;width:1200px;height:40px;background:var(--topbar);font-size:12px;color:var(--muted);padding:12px 16px}
.topbar .social{position:absolute;right:16px;top:11px;display:flex;gap:8px}
.square{width:16px;height:16px;background:#8a8a8a;display:block}

.header{left:0;top:40px;width:1200px;height:115px;background:var(--header)}
.brand{position:absolute;left:44px;top:28px;font-family:"Source Sans 3",sans-serif;font-weight:600;font-size:34px;letter-spacing:3px;line-height:1}
.brand small{display:block;font-size:15px;letter-spacing:5px;margin-top:4px}
.title{position:absolute;right:32px;top:24px;text-align:right}
.title h1{font-family:"Open Sans",sans-serif;font-style:italic;font-weight:700;font-size:41px;letter-spacing:1px;line-height:1.1}
.title p{font-family:"Source Sans 3",sans-serif;font-size:25px;color:var(--gold);font-weight:400}

.nav{left:0;top:155px;width:1200px;height:53px;background:#111;display:flex;padding-left:17px}
.nav a{color:#fff;text-decoration:none;font-size:16px;font-weight:600;letter-spacing:.5px;padding:0 20px;line-height:53px}
.nav a.active{background:var(--gold);width:95px;text-align:center;padding:0}

.hero-bg{left:0;top:208px;width:1200px;height:640px;background:radial-gradient(ellipse at 50% 40%,#4a4a4a 0%,#2c2c2c 55%,#202020 100%)}
.hero-media{left:146px;top:208px;width:908px;height:355px;background:linear-gradient(90deg,#3a3a3a 0%,#6b5a4a 45%,#7a4a3a 60%,#3c3c3c 100%);box-shadow:0 10px 30px rgba(0,0,0,.7)}
.player{left:146px;top:503px;width:908px;height:60px}
.slogan{left:0;top:583px;width:1200px;text-align:center;font-family:"Arvo",serif;font-weight:700;font-size:37px;letter-spacing:2px}
.lede{left:0;top:648px;width:1200px;text-align:center;font-family:"Source Sans 3",sans-serif;font-weight:300;font-size:33px;line-height:44px;color:#d8d8d8}
.lede b{color:var(--gold);font-weight:300}
.cta{left:449px;top:748px;width:289px;height:52px;background:var(--gold);display:flex;align-items:center;font-family:"Source Sans 3",sans-serif;font-size:31px;font-weight:300}
.cta svg{margin:0 38px 0 22px}

.feature{top:867px;height:192px;padding:18px 10px}
.feature.dark{background:var(--panel-dark)}
.feature.grey{background:var(--panel-grey)}
.feature h2{font-family:"Arvo",serif;font-size:27px;font-weight:400;display:flex;align-items:center;gap:14px;margin-bottom:10px;padding-left:6px}
.feature p{font-size:12px;line-height:19px;color:#e0e0e0;width:250px;padding-left:6px}
.btn-dark{position:absolute;left:10px;bottom:16px;width:124px;height:38px;background:#000;border:1px solid #555;display:flex;align-items:center;font-size:15px;gap:12px;padding-left:14px}

.about-media{left:46px;top:1089px;width:416px;height:202px;background:linear-gradient(180deg,#6e7a5a 0%,#5f8a3a 55%,#4f7a2a 100%)}
.about-bar{left:46px;top:1262px;width:416px;height:29px;background:#1d1d1d}
.about h2{font-family:"Arvo",serif;font-size:27px;font-weight:700;letter-spacing:1px}
.about{left:617px;top:1128px;width:560px}
.about p{font-size:13px;line-height:19px;color:#e6e6e6;margin-top:10px}
.btn-gold{background:var(--gold);display:flex;align-items:center;gap:14px;font-family:"Source Sans 3",sans-serif;font-size:20px;padding-left:14px}

.horses h2{font-family:"Arvo",serif;color:var(--gold);font-size:27px;font-weight:400;letter-spacing:1px}
.horses{left:18px;top:1360px}
.horses p{font-size:13px;margin-top:6px}
.arrows{left:17px;top:1437px;width:59px;height:20px;background:var(--gold)}
.tile{top:1458px;width:285px;height:202px}

.testimonial{left:17px;top:1726px;width:1160px;height:197px;background:rgba(30,30,30,.9);border-top:2px solid #555;padding:24px 19px}
.testimonial h2{font-family:"Arvo",serif;font-size:29px;font-weight:700;letter-spacing:1px}
.testimonial .who{font-family:"Source Sans 3",sans-serif;font-size:30px;color:var(--gold);font-weight:300;margin-top:6px}
.testimonial .who span{color:#fff;font-size:22px}
.testimonial p{font-size:15px;line-height:27px;color:#cfcfcf;width:1000px;margin-top:4px}

.footer{left:0;top:1978px;width:1200px;height:319px;background:var(--footer)}
.col{position:absolute;top:44px}
.col h3{font-family:"Arvo",serif;font-size:17px;font-weight:400;color:#d6d6d6;letter-spacing:1px;margin-bottom:26px}
.tweet{font-size:12px;line-height:20px;margin-bottom:20px;color:#e8e8e8}
.tweet .link{color:var(--gold)}
.tweet .date{color:#999;margin-left:6px}
.album{display:grid;grid-template-columns:repeat(4,46px);gap:12px 13px}
.album div{height:36px;background:linear-gradient(135deg,#5a4a3e,#8a8a8a);border:1px solid #888}
.contact p{font-size:12px;line-height:21px;color:#ddd}
.contact .mail{color:var(--gold)}
.phone{font-family:"Source Sans 3",sans-serif;font-size:30px;color:var(--gold);display:flex;align-items:center;gap:10px;margin-top:10px}
.field{background:#fff;color:#999;font-size:11px;text-align:center;height:26px;line-height:26px}
.bottom{left:0;top:2297px;width:1200px;height:50px;background:var(--bottom);border-top:2px solid #444;font-size:12px;color:#ccc;padding:18px 20px}
.bottom nav{position:absolute;right:58px;top:18px;display:flex;gap:8px}
.totop{position:absolute;right:8px;top:8px;width:36px;height:34px;background:#555}
</style>
</head>
<body>

<div class="abs topbar">
  <span>&#9679; 1800 Paddock Lane, UK &nbsp; &#9743; 1.555.010.2400</span>
  <div class="social"><span class="square"></span><span class="square"></span><span class="square"></span><span class="square"></span></div>
</div>

<header class="abs header">
  <div class="brand">COF<small>PARTNERS</small></div>
  <div class="title"><h1>Crest of Fortune</h1><p>Thoroughbred Racing Partnerships</p></div>
</header>

<nav class="abs nav">
  <a class="active">Home</a><a>About Us</a><a>Ownership</a><a>Stable Roster</a><a>News</a><a>Contact</a>
</nav>

<div class="abs hero-bg" role="img" aria-label="Dark cloudy sky over a racetrack"></div>
<div class="abs hero-media" role="img" aria-label="Video still of a pack of thoroughbreds and jockeys racing toward the camera"></div>
<svg class="abs player" width="908" height="60" viewBox="0 0 908 60">
  <path d="M6 180" fill="none"/>
  <polygon points="-4,0 0,0" />
  <polygon points="4,-84 16,-72 4,-60" fill="#fff" transform="translate(0,0)"/>
  <rect x="22" y="12" width="40" height="30" rx="3" fill="#111" opacity=".85"/>
  <polygon points="36,19 36,35 49,27" fill="#fff"/>
  <rect x="70" y="20" width="670" height="12" rx="2" fill="#111" opacity=".85"/>
  <rect x="76" y="23" width="214" height="6" fill="#2b8be0"/>
  <rect x="66" y="0" width="34" height="12" fill="#111"/>
  <text x="70" y="9" fill="#fff" font-size="9" font-family="Open Sans, sans-serif">00:00</text>
  <text x="800" y="31" fill="#2b8be0" font-size="12" font-weight="700" font-style="italic" font-family="Open Sans, sans-serif">HD</text>
</svg>
<svg class="abs" style="left:156px;top:374px" width="896" height="24" viewBox="0 0 896 24">
  <polyline points="10,6 4,12 10,18" fill="none" stroke="#fff" stroke-width="2"/>
  <polyline points="882,6 888,12 882,18" fill="none" stroke="#fff" stroke-width="2"/>
</svg>

<h2 class="abs slogan">Experience the thrill of owning a Racehorse</h2>
<p class="abs lede">Be a part of the thrilling event with just an<br>investment of as little as <b>$500</b></p>
<div class="abs cta">
  <svg width="26" height="18" viewBox="0 0 26 18"><path d="M2 9h18M13 2l8 7-8 7" fill="none" stroke="#fff" stroke-width="3"/><rect x="0" y="3" width="4" height="12" fill="#fff"/></svg>
  Know How
</div>

<section class="abs feature dark" style="left:8px;width:292px">
  <h2><svg width="26" height="26" viewBox="0 0 26 26"><circle cx="13" cy="8" r="6" fill="var(--gold)"/><path d="M1 26c0-8 5-11 12-11s12 3 12 11z" fill="var(--gold)"/></svg>Ownership</h2>
  <p>Lorem ipsum dolor sit amet, consectetur adipisicing elit, sed do eiusmod tempor incididunt ut labore</p>
  <div class="btn-dark">&#10140; Read More</div>
</section>
<section class="abs feature grey" style="left:303px;width:296px">
  <h2><svg width="28" height="26" viewBox="0 0 28 26"><polygon points="1,12 27,1 18,25 13,15" fill="var(--gold)"/></svg>Stable Roster</h2>
  <p>Lorem ipsum dolor sit amet, consectetur adipisicing elit, sed do eiusmod tempor incididunt ut labore</p>
  <div class="btn-dark">&#10140; Read More</div>
</section>
<section class="abs feature grey" style="left:602px;width:293px">
  <h2><svg width="24" height="30" viewBox="0 0 24 30"><path d="M0 0h16l8 8v22H0z" fill="var(--gold)"/><path d="M5 13h14M5 18h14M5 23h14" stroke="#333" stroke-width="2"/></svg>News</h2>
  <p>Lorem ipsum dolor sit amet, consectetur adipisicing elit, sed do eiusmod tempor incididunt ut labore</p>
  <div class="btn-dark">&#10140; Read More</div>
</section>
<section class="abs feature dark" style="left:899px;width:291px">
  <h2><svg width="28" height="28" viewBox="0 0 28 28"><rect x="2" y="4" width="24" height="22" rx="2" fill="none" stroke="var(--gold)" stroke-width="3"/><rect x="2" y="4" width="24" height="6" fill="var(--gold)"/><path d="M8 1v6M20 1v6" stroke="var(--gold)" stroke-width="3"/></svg>Events</h2>
  <p>Lorem ipsum dolor sit amet, consectetur adipisicing elit, sed do eiusmod tempor incididunt ut labore</p>
  <div class="btn-dark">&#10140; Read More</div>
</section>

<div class="abs about-media" role="img" aria-label="Video still of racehorses galloping along a green turf course"></div>
<div class="abs about-bar"></div>
<svg class="abs" style="left:218px;top:1141px" width="68" height="52" viewBox="0 0 68 52">
  <rect width="68" height="52" rx="8" fill="#222" opacity=".85"/><polygon points="26,14 26,38 46,26" fill="#fff"/>
</svg>
<div class="abs about">
  <h2>About Us</h2>
  <p>Lorem ipsum dolor sit amet, consectetur adipisicing elit, sed do eiusmod tempor incididunt ut labore et dolore magna aliqua. Ut enim ad minim veniam, quis nostrud exercitation ullamco laboris nisi ut aliquip ex ea commodo consequat.</p>
</div>
<div class="abs btn-gold" style="left:981px;top:1235px;width:172px;height:38px">&#10140; Read More</div>

<div class="abs horses">
  <h2>The Horses of Choice</h2>
  <p>Lorem ipsum dolor sit amet, consectetur adipisicing elit, sed do eiusmod tempor incididunt ut</p>
</div>
<svg class="abs arrows" width="59" height="20" viewBox="0 0 59 20">
  <path d="M10 10h14M10 10l5-5M10 10l5 5M35 10h14M49 10l-5-5M49 10l-5 5" stroke="#fff" stroke-width="2" fill="none"/>
</svg>
<div class="abs tile" style="left:18px;background:linear-gradient(135deg,#e8e0d0,#8a4a20 60%,#3a2010)" role="img" aria-label="Chestnut racehorse head in bridle"></div>
<div class="abs tile" style="left:313px;background:linear-gradient(135deg,#9a9a9a,#3a3028 60%,#1a1a1a)" role="img" aria-label="Dark bay racehorse wearing a saddle cloth"></div>
<div class="abs tile" style="left:604px;background:linear-gradient(135deg,#5a3a30,#a04a40 55%,#2a1a14)" role="img" aria-label="Racehorse wearing a red hood and blinkers"></div>
<div class="abs tile" style="left:894px;background:linear-gradient(135deg,#3a2a18,#c0a070 55%,#f0e0c0)" role="img" aria-label="Pale horse with flowing mane"></div>

<section class="abs testimonial">
  <h2>See what our&nbsp; Partners are saying</h2>
  <div class="who">Miles Hartwell, <span>CEO. Brightmoor Holdings</span></div>
  <p>Lorem ipsum dolor sit amet, consectetur adipisicing elit, sed do eiusmod tempor incididunt ut labore et dolore magna aliqua. Ut enim ad minim veniam, quis nostrud exercitation ullamco laboris nisi ut aliquip ex ea commodo consequat.</p>
</section>
<div class="abs btn-gold" style="left:909px;top:1872px;width:244px;height:38px">&#10140; View All Testimonials</div>

<footer class="abs footer">
  <div class="col" style="left:17px;width:270px">
    <h3>Latest Tweets</h3>
    <div class="tweet">&#9656; Lorem ipsum dolor sit ---- I am Owen<br><span class="link">http://clips.example/cof-race-01</span><span class="date">2013/10/24</span></div>
    <div class="tweet">&#9656; Lorem ipsum dolor sit ---- I am Owen<br><span class="link">http://clips.example/cof-race-01</span><span class="date">2013/10/24</span></div>
    <div class="tweet">&#9656; Lorem ipsum dolor sit ---- I am Owen<br><span class="link">http://clips.example/cof-race-01</span><span class="date">2013/10/24</span></div>
    <div class="tweet">&#9656; Lorem ipsum dolor sit ---- I am Owen<br><span class="link">http://clips.example/cof-race-01</span><span class="date">2013/10/24</span></div>
  </div>
  <div class="col" style="left:314px">
    <h3>Latest Album</h3>
    <div class="album" role="img" aria-label="Thumbnail gallery of racing photos">
      <div></div><div></div><div></div><div></div><div></div><div></div><div></div><div></div><div></div><div></div><div></div><div></div>
    </div>
  </div>
  <div class="col contact" style="left:617px">
    <h3>Get In Touch</h3>
    <p>72 Harrow Ridge Road<br>Fernvale, MO 60000</p>
    <p class="mail">&#9993; hello@crestoffortune.example</p>
    <div class="phone"><svg width="24" height="46" viewBox="0 0 24 46"><rect x="2" y="2" width="20" height="42" rx="4" fill="none" stroke="#aaa" stroke-width="3"/><rect x="6" y="8" width="12" height="24" fill="#aaa"/></svg>155501024000</div>
    <div style="display:flex;gap:10px;margin-top:14px"><span class="square" style="width:14px;height:14px"></span><span class="square" style="width:14px;height:14px"></span><span class="square" style="width:14px;height:14px"></span><span class="square" style="width:14px;height:14px"></span></div>
  </div>
  <div class="col" style="left:907px;width:270px">
    <h3>Quick Contact</h3>
    <div style="display:flex;justify-content:space-between"><div class="field" style="width:122px">Name</div><div class="field" style="width:122px">Email</div></div>
    <div class="field" style="height:100px;margin-top:8px;text-align:left;padding-left:8px">Message</div>
    <div style="margin:10px 0 0 163px;width:107px;height:38px;background:#000;display:flex;align-items:center;gap:12px;padding-left:12px;font-size:14px">&#10140; Submit</div>
  </div>
</footer>

<div class="abs bottom">
  @Copyright message
  <nav><span>Home</span><span>About Us</span><span>Ownership</span><span>Stable Roster</span><span>News</span><span>Contact</span></nav>
  <div class="totop"></div>
</div>

</body>
</html>
```